Irrigation Business needs their business cards modernised and revamped

I would like to keep my current logo, colours and revamp the format of the card.

I would like the card to be clean yet important.

Im not sure if you include texture but i would like the named logo to be indented into the card etc.

show me something alive and free something thats clinical to the point yet has a feel of achievement. i would like people to go nice card.

Target Market(s)

high end clients, corporate, sports field manger, the guys that make the decisions

Industry/Entity Type

Business

Contact Information for Business Card

nformation to be included

Dorian Hesk (Director)
0487253916
dorian@tfcraft.biz
www.taddsfieldcrafts.com

instagram logo
google logo
facebook logo

Colors

Designer to choose colors to be used in the design.

Requirements
Nice to have
• indentations a really nice feel to the card good texture

```html
<!DOCTYPE html>
<html lang="en">
<head>
<meta charset="utf-8">
<title>Tadd's Irrigation Services – Business Card</title>
<link rel="stylesheet" href="https://fonts.googleapis.com/css2?family=Arimo:wght@700&family=Open+Sans:wght@400;600&display=swap">
<style>
  :root {
    --backdrop: #383838;
    --card-white: #ffffff;
    --sky-blue: #31a6d8;
    --deep-blue: #2a5ea8;
    --ink: #3a3a3a;
    --icon-grey: #d9d9d9;
  }
  * { margin: 0; padding: 0; box-sizing: border-box; }
  html, body { width: 1200px; height: 900px; overflow: hidden; }
  body { background: var(--backdrop); position: relative; font-family: "Open Sans", Arial, sans-serif; }

  .card {
    position: absolute;
    top: 306px;
    width: 440px;
    height: 271px;
    border-radius: 10px;
    overflow: hidden;
  }
  .card--front { left: 149px; background: var(--card-white); }
  .card--back { left: 608px; background: var(--sky-blue); }

  .front-band {
    position: absolute;
    left: 368px; top: 0;
    width: 72px; height: 100%;
    background: var(--sky-blue);
  }
  .front-seal {
    position: absolute;
    left: 305px; top: 77px;
    width: 118px; height: 118px;
    border-radius: 50%;
    background: var(--card-white);
    border: 5px solid var(--deep-blue);
    box-shadow: 0 0 0 4px var(--card-white);
  }

  .company-name {
    font-family: "Arimo", Arial, sans-serif;
    font-weight: 700;
    text-align: center;
    line-height: 1;
  }
  .company-name__line1 { display: block; letter-spacing: -0.5px; }
  .company-name__line2 { display: block; letter-spacing: 6px; }

  .card--front .company-name {
    position: absolute;
    left: 22px; top: 36px;
    width: 270px;
    color: var(--deep-blue);
  }
  .card--front .company-name__line1 { font-size: 27px; }
  .card--front .company-name__line2 { font-size: 17px; margin-top: 6px; padding-left: 6px; }

  .holder { position: absolute; left: 25px; top: 150px; }
  .holder__name {
    font-weight: 600; font-size: 15px; color: var(--deep-blue);
    text-transform: uppercase; letter-spacing: 0.2px;
  }
  .holder__role { font-size: 11px; color: var(--ink); margin-top: -2px; }

  .contacts { position: absolute; left: 24px; top: 196px; list-style: none; }
  .contacts li {
    display: flex; align-items: center; gap: 3px;
    font-size: 12px; color: var(--ink); height: 16px;
  }
  .contacts svg { width: 12px; height: 12px; flex: none; }

  .back-seal {
    position: absolute;
    left: 172px; top: 58px;
    width: 96px; height: 96px;
    border-radius: 50%;
    border: 3px solid var(--card-white);
  }
  .card--back .company-name {
    position: absolute;
    left: 0; top: 165px; width: 100%;
    color: var(--card-white);
  }
  .card--back .company-name__line1 { font-size: 29px; }
  .card--back .company-name__line2 { font-size: 18px; margin-top: 6px; padding-left: 6px; }

  .social { position: absolute; left: 182px; top: 228px; display: flex; gap: 5px; }
  .social span {
    width: 21px; height: 21px; border-radius: 50%;
    background: var(--icon-grey);
  }
</style>
</head>
<body>
  <section class="card card--front" aria-label="Business card front">
    <div class="front-band"></div>
    <div class="front-seal"></div>
    <h1 class="company-name">
      <span class="company-name__line1">TADD'S IRRIGATION</span>
      <span class="company-name__line2">SERVICES</span>
    </h1>
    <div class="holder">
      <p class="holder__name">Dorian Hesk</p>
      <p class="holder__role">Director</p>
    </div>
    <ul class="contacts">
      <li>
        <svg viewBox="0 0 12 12"><circle cx="6" cy="6" r="6" fill="#2a5ea8"/><path d="M3 5.2c0-1 1-1.6 3-1.6s3 .6 3 1.6H7.7v-.6H4.3v.6zM4 5.6h4l.6 2.6H3.4z" fill="#fff"/></svg>
        0487253916
      </li>
      <li>
        <svg viewBox="0 0 12 12"><circle cx="6" cy="6" r="6" fill="#2a5ea8"/><rect x="3" y="3.8" width="6" height="4.4" fill="#fff"/><path d="M3 3.8l3 2.4 3-2.4" fill="none" stroke="#2a5ea8" stroke-width=".7"/></svg>
        dorian@tfcraft.biz
      </li>
      <li>
        <svg viewBox="0 0 12 12"><circle cx="6" cy="6" r="6" fill="#2a5ea8"/><circle cx="6" cy="6" r="3" fill="none" stroke="#fff" stroke-width=".8"/><path d="M3 6h6M6 3c-1.4 1.6-1.4 4.4 0 6M6 3c1.4 1.6 1.4 4.4 0 6" fill="none" stroke="#fff" stroke-width=".6"/></svg>
        www.taddsfieldcrafts.com
      </li>
    </ul>
  </section>

  <section class="card card--back" aria-label="Business card back">
    <div class="back-seal"></div>
    <h2 class="company-name">
      <span class="company-name__line1">TADD'S IRRIGATION</span>
      <span class="company-name__line2">SERVICES</span>
    </h2>
    <div class="social" aria-label="Social profiles">
      <span></span><span></span><span></span>
    </div>
  </section>
</body>
</html>
```